Business Card Design Project

I need a business card designed for FableHarbor, a website which has people share their fictional story ideas with others. The business cards should incorporate the websites's logo, which can be found at www.fableharbor-example.com .

Target Market(s)

These will be primarily used in business development activities, not given to customers. It therefore needs to have a clean, professional appearance, and yet communicate what the company is trying to achieve as a bold startup.

Industry/Entity Type

Business

```html
<!DOCTYPE html>
<html lang="en">
<head>
<meta charset="utf-8">
<title>FableHarbor Business Cards</title>
<link rel="stylesheet" href="https://fonts.googleapis.com/css2?family=Exo+2:wght@500;600&family=Arimo&display=swap">
<style>
  :root {
    --page: #ffffff;
    --navy: #17486a;
    --steel: #3a6f96;
    --mist: #d2e3f2;
    --ink: #ffffff;
    --soft-ink: #dfe9f2;
  }
  * { box-sizing: border-box; margin: 0; padding: 0; }
  html, body { width: 1200px; height: 761px; overflow: hidden; background: var(--page); }
  .canvas { position: relative; width: 1200px; height: 761px; }

  .card {
    position: absolute;
    width: 457px;
    height: 261px;
    background: var(--navy);
    overflow: hidden;
  }
  .card--front-full { left: 121px; top: 71px; }
  .card--front-short { left: 630px; top: 71px; }
  .card--back { left: 342px; top: 409px; }

  .emblem-area { position: absolute; left: 0; top: 0; }

  .holder-name {
    position: absolute;
    top: 20px;
    font-family: "Exo 2", sans-serif;
    font-weight: 500;
    font-size: 20px;
    color: var(--ink);
    letter-spacing: 0.2px;
    white-space: nowrap;
  }
  .holder-role {
    position: absolute;
    top: 46px;
    font-family: "Arimo", sans-serif;
    font-size: 13px;
    color: var(--soft-ink);
  }
  .contact-list {
    position: absolute;
    top: 202px;
    list-style: none;
    font-family: "Arimo", sans-serif;
    font-size: 14px;
    color: var(--ink);
    line-height: 19px;
  }
  .contact-list li { display: flex; align-items: center; gap: 4px; }
  .contact-icon { width: 11px; height: 12px; flex: none; }

  .card--front-full .holder-name,
  .card--front-full .holder-role { left: 132px; }
  .card--front-full .contact-list { left: 126px; }
  .card--front-short .holder-name,
  .card--front-short .holder-role { left: 240px; }
  .card--front-short .contact-list { left: 146px; }

  .back-top {
    position: absolute; left: 0; top: 0; width: 100%; height: 169px;
    background: var(--navy);
  }
  .back-band {
    position: absolute; left: 0; top: 169px; width: 100%; height: 92px;
    background: var(--steel);
  }
  .brand-name {
    position: absolute; left: 0; right: 0; top: 38px;
    text-align: center;
    font-family: "Exo 2", sans-serif;
    font-weight: 600;
    font-size: 42px;
    color: var(--ink);
    letter-spacing: 0.5px;
  }
  .brand-url {
    position: absolute; left: 0; right: 0; top: 99px;
    display: flex; justify-content: center; align-items: center; gap: 4px;
    font-family: "Arimo", sans-serif;
    font-size: 14px;
    color: var(--soft-ink);
  }
  .feature-icons {
    position: absolute; left: 0; top: 0; width: 100%; height: 92px;
  }
</style>
</head>
<body>
<main class="canvas">

  <section class="card card--front-full" aria-label="Front of card, full name">
    <svg class="emblem-area" width="140" height="261" role="img" aria-label="Large brand emblem in light blue half circle">
      <circle cx="4" cy="130" r="131" fill="var(--steel)"/>
    </svg>
    <h1 class="holder-name">Daniel Augusto Moreira</h1>
    <p class="holder-role">Founder</p>
    <ul class="contact-list">
      <li>
        <svg class="contact-icon" viewBox="0 0 11 12"><rect x="3" y="1" width="5" height="10" rx="1" fill="none" stroke="var(--ink)" stroke-width="1.2"/></svg>
        +1(555)014-2260
      </li>
      <li>
        <svg class="contact-icon" viewBox="0 0 11 12"><rect x="1" y="4" width="9" height="6" fill="none" stroke="var(--ink)" stroke-width="1.2"/><path d="M1 4 L5.5 7.5 L10 4" fill="none" stroke="var(--ink)" stroke-width="1.2"/></svg>
        daniel@fableharbor-example.com
      </li>
    </ul>
  </section>

  <section class="card card--front-short" aria-label="Front of card, short name">
    <svg class="emblem-area" width="180" height="261" role="img" aria-label="Large brand emblem in light blue half circle">
      <circle cx="47" cy="130" r="131" fill="var(--steel)"/>
    </svg>
    <h1 class="holder-name">Daniel A Moreira</h1>
    <p class="holder-role">Founder</p>
    <ul class="contact-list">
      <li>
        <svg class="contact-icon" viewBox="0 0 11 12"><rect x="3" y="1" width="5" height="10" rx="1" fill="none" stroke="var(--ink)" stroke-width="1.2"/></svg>
        +1(555)014-2260
      </li>
      <li>
        <svg class="contact-icon" viewBox="0 0 11 12"><rect x="1" y="4" width="9" height="6" fill="none" stroke="var(--ink)" stroke-width="1.2"/><path d="M1 4 L5.5 7.5 L10 4" fill="none" stroke="var(--ink)" stroke-width="1.2"/></svg>
        daniel@fableharbor-example.com
      </li>
    </ul>
  </section>

  <section class="card card--back" aria-label="Back of card">
    <div class="back-top">
      <p class="brand-name">FableHarbor</p>
      <p class="brand-url">
        <svg class="contact-icon" viewBox="0 0 12 12"><circle cx="6" cy="6" r="4.5" fill="none" stroke="var(--soft-ink)" stroke-width="1.1"/><path d="M1.5 6 H10.5 M6 1.5 V10.5" stroke="var(--soft-ink)" stroke-width="1"/></svg>
        www.fableharbor-example.com
      </p>
    </div>
    <div class="back-band">
      <svg class="feature-icons" viewBox="0 0 457 92">
        <g class="feature feature--write">
          <circle cx="132" cy="46" r="30" fill="var(--mist)" stroke="var(--navy)" stroke-width="1.5"/>
          <path d="M128 38 H118 V60 H140 V50" fill="none" stroke="var(--navy)" stroke-width="3"/>
          <path d="M126 52 L144 34 L148 38 L130 56 L125 57 Z" fill="var(--navy)"/>
        </g>
        <g class="feature feature--talk">
          <circle cx="228" cy="46" r="30" fill="var(--mist)" stroke="var(--navy)" stroke-width="1.5"/>
          <rect x="215" y="34" width="20" height="14" rx="6" fill="none" stroke="var(--navy)" stroke-width="2.5"/>
          <path d="M219 48 L217 54 L224 48" fill="var(--navy)"/>
          <path d="M237 40 H239 A5 5 0 0 1 244 45 V49 A5 5 0 0 1 239 54 H236 L240 59 L230 54 H228" fill="none" stroke="var(--navy)" stroke-width="2.5"/>
        </g>
        <g class="feature feature--favourite">
          <circle cx="325" cy="46" r="30" fill="var(--mist)" stroke="var(--navy)" stroke-width="1.5"/>
          <path d="M325 32 L329 42 L339 42.5 L331 49 L334 59 L325 53.5 L316 59 L319 49 L311 42.5 L321 42 Z" fill="none" stroke="var(--navy)" stroke-width="2.5" stroke-linejoin="round"/>
        </g>
      </svg>
    </div>
  </section>

</main>
</body>
</html>
```